Bright Fern Property Services

Design a billboard with our logo that includes bullet points for
Property Maintenance, Plumbing, and Electrical, licensed and insured.
Phone number 865 471 3908

also add the website brightfernps-example.com

```html
<!DOCTYPE html>
<html lang="en">
<head>
<meta charset="utf-8">
<title>Bright Fern Property Services – Billboard</title>
<link href="https://fonts.googleapis.com/css2?family=Poppins:wght@500;600;700&display=swap" rel="stylesheet">
<style>
  :root {
    --backdrop: #232323;
    --band-black: #000000;
    --fern-green: #4fa924;
    --deep-green: #2f7d1a;
    --ink: #0b0b0b;
    --white: #ffffff;
    --wood-light: #efe0c6;
    --wood-mid: #e2cfae;
    --wood-dark: #d6c09b;
  }
  * { box-sizing: border-box; margin: 0; padding: 0; }
  html, body {
    width: 1200px; height: 1200px; overflow: hidden;
    background: var(--backdrop);
    font-family: "Poppins", sans-serif;
  }
  .billboard {
    position: absolute; left: 22px; top: 371px;
    width: 1156px; height: 492px;
    display: flex; flex-direction: column;
  }
  .credential-band {
    height: 67px; background: var(--band-black);
    display: flex; align-items: center; justify-content: center;
  }
  .credential-band p {
    color: var(--white); font-weight: 500; font-size: 40px;
    letter-spacing: 0.45em; padding-left: 0.45em; line-height: 1;
  }
  .main-panel {
    position: relative; height: 343px; overflow: hidden;
  }
  .wood-surface {
    position: absolute; inset: 0;
    background: radial-gradient(ellipse at 85% 80%, var(--wood-dark) 0%, var(--wood-mid) 35%, var(--wood-light) 75%);
  }
  .brand-name {
    position: absolute; left: 36px; top: 80px;
    color: var(--fern-green); font-weight: 600;
    font-size: 108px; line-height: 1; letter-spacing: 0.005em;
    text-transform: uppercase; white-space: nowrap;
  }
  .brand-descriptor {
    position: absolute; left: 59px; top: 209px;
    color: var(--ink); font-weight: 600;
    font-size: 48px; line-height: 1; letter-spacing: 0.22em;
    text-transform: uppercase; white-space: nowrap;
  }
  .brand-rule {
    position: absolute; left: 59px; top: 284px; width: 552px; height: 2px;
    background: var(--fern-green);
  }
  .brand-suffix {
    position: absolute; right: 433px; top: 262px;
    color: var(--ink); font-weight: 600; font-size: 40px;
    letter-spacing: 0.14em; line-height: 1;
  }
  .service-list { list-style: none; }
  .service-item {
    position: absolute; left: 773px;
    display: flex; align-items: center; gap: 14px;
  }
  .service-item.maintenance { top: 69px; }
  .service-item.plumbing { top: 182px; }
  .service-item.electrical { top: 249px; }
  .service-icon { width: 54px; height: 54px; flex: none; }
  .service-label {
    font-weight: 600; font-size: 40px; line-height: 1;
    color: var(--ink); text-transform: uppercase; letter-spacing: -0.01em;
  }
  .contact-band {
    height: 82px; background: var(--fern-green);
    display: flex; align-items: center; padding: 0 14px; gap: 12px;
    color: var(--ink); font-weight: 700; white-space: nowrap;
  }
  .contact-icon.phone { width: 34px; height: 34px; flex: none; }
  .contact-icon.globe { width: 44px; height: 44px; flex: none; }
  .contact-phone { font-size: 54px; line-height: 1; letter-spacing: -0.03em; }
  .contact-divider { font-size: 50px; line-height: 1; margin: 0 8px 0 0; }
  .contact-web { font-size: 33px; line-height: 1; letter-spacing: -0.02em; }
</style>
</head>
<body>
<main class="billboard">
  <header class="credential-band"><p>LICENSED AND INSURED</p></header>

  <section class="main-panel">
    <div class="wood-surface" role="img" aria-label="Light oak wood grain background with tree rings"></div>

    <p class="brand-name">Bright Fern</p>
    <p class="brand-descriptor">Property Services</p>
    <div class="brand-rule"></div>
    <p class="brand-suffix">LLC</p>

    <ul class="service-list">
      <li class="service-item maintenance">
        <svg class="service-icon" viewBox="0 0 54 54">
          <circle cx="27" cy="27" r="26" fill="var(--white)"/>
          <circle cx="27" cy="27" r="23" fill="var(--deep-green)"/>
          <path d="M16 28 L27 18 L38 28 M20 25 V37 H34 V25" fill="none" stroke="var(--white)" stroke-width="2.5" stroke-linejoin="round"/>
          <rect x="24.5" y="29" width="5" height="8" fill="var(--white)"/>
        </svg>
        <span class="service-label">Property<br>Maintenance</span>
      </li>
      <li class="service-item plumbing">
        <svg class="service-icon" viewBox="0 0 54 54">
          <circle cx="27" cy="27" r="26" fill="var(--white)"/>
          <circle cx="27" cy="27" r="23" fill="var(--deep-green)"/>
          <path d="M15 22 H33 Q38 22 38 27 V30" fill="none" stroke="var(--white)" stroke-width="4"/>
          <rect x="22" y="15" width="4" height="7" fill="var(--white)"/>
          <path d="M38 33 Q36 37 38 39 Q40 37 38 33 Z" fill="var(--white)"/>
          <rect x="17" y="26" width="4" height="15" rx="1.5" fill="var(--white)"/>
        </svg>
        <span class="service-label">Plumbing</span>
      </li>
      <li class="service-item electrical">
        <svg class="service-icon" viewBox="0 0 54 54">
          <circle cx="27" cy="27" r="26" fill="var(--white)"/>
          <circle cx="27" cy="27" r="23" fill="var(--deep-green)"/>
          <circle cx="27" cy="27" r="14" fill="none" stroke="var(--white)" stroke-width="2.5"/>
          <path d="M29 17 L22 29 H27 L25 37 L32 25 H27 Z" fill="var(--white)"/>
        </svg>
        <span class="service-label">Electrical</span>
      </li>
    </ul>
  </section>

  <footer class="contact-band">
    <svg class="contact-icon phone" viewBox="0 0 38 38">
      <path d="M9 5 L15 5 L17 13 L13 16 Q16 23 22 26 L25 22 L33 24 L33 30 Q32 34 28 34 Q8 31 5 10 Q5 6 9 5 Z" fill="var(--white)"/>
      <path d="M22 5 A11 11 0 0 1 33 16 M22 10 A6 6 0 0 1 28 16" fill="none" stroke="var(--white)" stroke-width="2"/>
    </svg>
    <span class="contact-phone">865 471 3908</span>
    <span class="contact-divider">|</span>
    <svg class="contact-icon globe" viewBox="0 0 38 38">
      <g fill="none" stroke="var(--white)" stroke-width="2">
        <circle cx="18" cy="18" r="15"/>
        <ellipse cx="18" cy="18" rx="6.5" ry="15"/>
        <path d="M3 18 H33 M6 10 H30 M6 26 H30"/>
      </g>
      <path d="M24 24 L36 29 L31 31 L29 36 Z" fill="var(--white)" stroke="var(--fern-green)" stroke-width="1.5"/>
    </svg>
    <span class="contact-web">WWW.BRIGHTFERNPS-EXAMPLE.COM</span>
  </footer>
</main>
</body>
</html>
```